Harbor Grace Chapel Stationary and PPT template

Harbor Grace Chapel, an english-speaking church in urban Tokyo, Japan seeks a letterhead, envelope, and powerpoint background to communicate it's brand across all written and digital communications. The successful design should be conservative and classic in keeping with the church's long history as a beacon of light in Tokyo. A branding style guide should be consulted but designs should not emulate the mock design in the guide.

Designs should be classic and in keeping with the logo usage per the style guide. Colours should be faithful to the turquoise of the HGC brand.

The church website can be consulted for more information regarding phone numbers, address, etc.

Paper size- A4
Envelope size- DL
PPT Template- Mostly white background, colours at bottom + logo.

Target Market(s)

Outside vendors, members, prospective members.

Industry/Entity Type

Church

Requirements
Must have
• Church Logo, Address, phone, office email, white background.
Should not have
• contemporary look and feel. Must be classic design

```html
<!DOCTYPE html>
<html lang="en">
<head>
<meta charset="utf-8">
<title>Harbor Grace Chapel – Stationery</title>
<link rel="stylesheet" href="https://fonts.googleapis.com/css2?family=Open+Sans:ital,wght@0,400;0,600;1,400&family=Gelasio:ital,wght@1,400;1,500&display=swap">
<style>
  :root {
    --teal: #5bb8bd;
    --paper: #ffffff;
    --paper-tint: #eef5f4;
    --ink: #2b2b2b;
    --backdrop: #e9eaec;
  }
  * { box-sizing: border-box; margin: 0; padding: 0; }
  html, body { width: 1200px; height: 1200px; overflow: hidden; }
  body {
    background: var(--backdrop);
    font-family: "Open Sans", Arial, sans-serif;
    color: var(--ink);
    position: relative;
  }
  .sheet { position: absolute; background: var(--paper); overflow: hidden; }

  /* brand lockup */
  .brand { position: absolute; display: flex; flex-direction: column; align-items: center; }
  .brand-mark { width: 12px; height: 12px; background: var(--teal); }
  .brand-name {
    color: var(--teal); font-weight: 600; letter-spacing: 0.08em;
    text-transform: uppercase; white-space: nowrap; line-height: 1.3;
  }
  .brand-tagline {
    color: var(--teal); border-top: 1px solid var(--teal);
    white-space: nowrap; text-align: center; line-height: 1.3;
  }

  /* business cards */
  .card { top: 300px; width: 186px; height: 106px; }
  .card--front { left: 138px; background: var(--teal); }
  .card--back { left: 352px; background: var(--paper-tint); }
  .card .brand { left: 0; right: 0; top: 20px; }
  .card .brand-mark { margin-bottom: 36px; }
  .card .brand-name { font-size: 6.5px; }
  .card .brand-tagline { font-size: 6px; margin-top: 3px; padding-top: 3px; width: 74px; }
  .card--front .brand-mark { background: #fff; }
  .card--front .brand-name, .card--front .brand-tagline { color: #fff; border-color: #fff; }

  /* accent bands */
  .band { position: absolute; background: var(--teal); }

  /* contact block */
  .contact { position: absolute; font-size: 6.2px; line-height: 1.35; color: var(--ink); font-style: normal; }
  .contact-title { color: var(--teal); font-weight: 600; }
  .contact-gap { height: 6px; }
  .contact-key { color: var(--teal); font-weight: 600; }

  /* envelopes */
  .envelope { left: 138px; width: 400px; height: 198px; }
  .envelope--front { top: 436px; }
  .envelope--front .brand { left: 10px; top: 16px; width: 90px; }
  .envelope--front .brand-mark { margin-bottom: 34px; }
  .envelope--front .brand-name { font-size: 6.3px; }
  .envelope--front .brand-tagline { font-size: 5.6px; margin-top: 3px; padding-top: 3px; width: 72px; }
  .envelope--front .contact { left: 10px; top: 120px; }

  .envelope--back { top: 668px; }
  .envelope-flap {
    position: absolute; left: 0; top: 0; width: 100%; height: 50px;
    background: var(--teal);
    clip-path: polygon(0 0, 100% 0, 100% 30%, 97% 100%, 3% 100%, 0 30%);
  }

  /* letterhead */
  .letterhead { left: 588px; top: 300px; width: 402px; height: 566px; }
  .letterhead .brand { left: 28px; top: 44px; width: 90px; }
  .letterhead .brand-mark { width: 14px; height: 14px; margin-bottom: 48px; }
  .letterhead .brand-name { font-size: 7px; }
  .letterhead .brand-tagline { font-size: 7px; margin-top: 4px; padding-top: 4px; width: 90px; text-align: center; }
  .letter-date {
    position: absolute; right: 30px; top: 104px; width: 92px;
    font-family: "Gelasio", Georgia, serif; font-style: italic; font-size: 7.5px;
    border-bottom: 1px solid var(--teal); padding: 0 0 3px 4px;
  }
  .letter-date sup { font-size: 5px; }
  .letter-body { position: absolute; left: 30px; right: 38px; top: 150px; }
  .letter-heading { color: var(--teal); font-weight: 400; font-size: 14px; line-height: 19px; margin-bottom: 5px; }
  .letter-quote {
    font-family: "Gelasio", Georgia, serif; font-style: italic; font-size: 11.4px;
    line-height: 18px; margin-bottom: 12px;
  }
  .letter-text { font-size: 6.4px; line-height: 14px; margin-bottom: 12px; }
  .letter-text--lead { margin-bottom: 4px; }
  .letter-list { list-style: none; font-size: 6.4px; line-height: 12px; }
  .letter-list li { position: relative; padding-left: 6px; }
  .letter-list li::before {
    content: ""; position: absolute; left: 0; top: 5px; width: 2.5px; height: 2.5px; background: var(--teal);
  }
  .letterhead .contact { left: 40px; top: 460px; }
</style>
</head>
<body>

  <section class="sheet card card--front" aria-label="Business card, front">
    <div class="brand">
      <span class="brand-mark"></span>
      <span class="brand-name">Harbor Grace Chapel</span>
      <span class="brand-tagline">Anchored in His grace</span>
    </div>
  </section>

  <section class="sheet card card--back" aria-label="Business card, back">
    <div class="brand">
      <span class="brand-mark"></span>
      <span class="brand-name">Harbor Grace Chapel</span>
      <span class="brand-tagline">Anchored in His grace</span>
    </div>
  </section>

  <section class="sheet envelope envelope--front" aria-label="DL envelope, front">
    <div class="band" style="right:0; top:0; width:128px; height:9px;"></div>
    <div class="brand">
      <span class="brand-mark"></span>
      <span class="brand-name">Harbor Grace Chapel</span>
      <span class="brand-tagline">Anchored in His grace</span>
    </div>
    <address class="contact">
      <div class="contact-title">Our Chapel:</div>
      <div>Harbor Grace Chapel,</div>
      <div>2-14-3 Minato-cho, Chuo-ku,</div>
      <div>Tokyo 104-0041</div>
      <div class="contact-gap"></div>
      <div><span class="contact-key">T:</span> +81 3-5550-0123</div>
      <div><span class="contact-key">F:</span> +81 3-5550-0456</div>
      <div><span class="contact-key">E:</span> office@harborgrace.org</div>
    </address>
    <div class="band" style="left:0; bottom:0; width:128px; height:8px;"></div>
  </section>

  <section class="sheet envelope envelope--back" aria-label="DL envelope, back">
    <div class="envelope-flap"></div>
  </section>

  <section class="sheet letterhead" aria-label="A4 letterhead">
    <div class="band" style="right:0; top:0; width:133px; height:8px;"></div>
    <div class="brand">
      <span class="brand-mark"></span>
      <span class="brand-name">Harbor Grace Chapel</span>
      <span class="brand-tagline">Anchored in His grace</span>
    </div>
    <div class="letter-date">Date:&nbsp; Nov 12<sup>th</sup>, 2017</div>

    <div class="letter-body">
      <h2 class="letter-heading">What We Believe</h2>
      <p class="letter-quote">"A welcoming family of faithful believers by the Tokyo harbor, carrying the hope of Christ to every nation."</p>

      <h2 class="letter-heading">Introduction</h2>
      <p class="letter-text">Harbor Grace Chapel began as a small gathering of seafarers and merchants and has grown into an interdenominational, international fellowship of English-speaking believers. Our name reflects the conviction that all who gather here, whatever their tradition or homeland, are held together by the grace of the Lord Jesus Christ. Our members bring the gifts of their own backgrounds into worship, friendship and service. Harbor Grace Chapel is self-governing and supported entirely by its members.</p>

      <h2 class="letter-heading">What characterizes our church</h2>
      <p class="letter-text letter-text--lead">The people of Harbor Grace Chapel are called to live as witnesses of God's faithful love in Jesus Christ our Lord, walking in daily obedience:</p>
      <ul class="letter-list">
        <li>we gather to worship the one true and living God;</li>
        <li>we proclaim the good news of Christ, who brings new life to all;</li>
        <li>and, led by the Holy Spirit, we share in and are upheld by a fellowship of care, service and prayer.</li>
      </ul>
    </div>

    <address class="contact">
      <div class="contact-title">Our Chapel:</div>
      <div>Harbor Grace Chapel,</div>
      <div>2-14-3 Minato-cho, Chuo-ku,</div>
      <div>Tokyo 104-0041</div>
      <div class="contact-gap"></div>
      <div><span class="contact-key">T:</span> +81 3-5550-0123</div>
      <div><span class="contact-key">F:</span> +81 3-5550-0456</div>
      <div><span class="contact-key">E:</span> office@harborgrace.org</div>
    </address>
    <div class="band" style="left:0; bottom:0; width:133px; height:8px;"></div>
  </section>

</body>
</html>
```